personal development e-book needs book cover design

We need a book design for a new personal development course called 'Copper Lantern Path'.

The course offers insights into how people can overcome negative, fear based mindsets to create the ultimate mindset empowering them to achieve huge success in their lives.

To be included on cover:
Title: Copper Lantern Path
Sub-title: Empower your mind to live fearlessly, creating a life full of wealth, health and success.

Reference information
– What book/course is about
Discover Ancient Ninja Secrets to create the ultimate mindset and unleash your inner ninja. The book explains how to create this mindset and more, including:
* Overcome guilt, fear and self-doubt
* Understand that the right mindset is more critical to your success than talent
* Break free from childhood programming that is holding you back
* Stop being the victim
* Take responsibility and take control of your life
* Understand that while you can be your own worst enemy, you can also be your own best friend
* Learn to love yourself
* Find success in all areas of your life
* Help and inspire others, instead of dragging them down

Target Market(s)

self-help niche. 40-55 year old.

Font styles to use
Other font styles liked:
• Asian fonts - for example 'Last Ninja'.

Colors
0592cd
33a6d7
3276b5
f04a50
ffffff
ec1f27
000000

Requirements
Must have
• A Ninja.
Nice to have
• If you can somehow convey the idea of mindset into the cover that would be good. Copper Lantern Path is the ultimate mindset so I want the cover to be powerful and convey that sense to the reader. If you can build some intrigue into the image as well that would be fantastic.
• Quote pull-outs in the book are blue, so while its not necessary to have blue on the cover, it would be consistent with the colour scheme in the book. I have chosen some colours that could be used on the cover below. (white, black and greys are fine too). It really does depend on the design.
Should not have
• Just a stock image with text overlay will not be chosen. I want some originality please.

```html
<!DOCTYPE html>
<html lang="en">
<head>
<meta charset="utf-8">
<title>Copper Lantern Path — Book Cover</title>
<link href="https://fonts.googleapis.com/css2?family=Cinzel:wght@400;500;600&display=swap" rel="stylesheet">
<style>
  :root {
    --backdrop: #111111;
    --parchment: #ecccA6;
    --ink: #050505;
    --crimson: #d8121c;
    --crimson-light: #f04a50;
    --crimson-deep: #9a0c12;
    --gold-text: #e6c393;
  }
  * { box-sizing: border-box; margin: 0; padding: 0; }
  html, body {
    width: 1200px;
    height: 670px;
    overflow: hidden;
    background: var(--backdrop);
  }
  .canvas {
    position: relative;
    width: 1200px;
    height: 670px;
    background: var(--backdrop);
  }
  .book-cover {
    position: absolute;
    left: 400px;
    top: 53px;
    width: 398px;
    height: 563px;
    background: var(--parchment);
    overflow: hidden;
    box-shadow: 0 10px 30px rgba(0,0,0,0.6);
  }
  .title {
    position: absolute;
    top: 38px;
    left: 0;
    width: 100%;
    text-align: center;
    font-family: "Cinzel", serif;
    color: var(--ink);
    font-weight: 500;
  }
  .title-lead {
    display: block;
    font-size: 25px;
    line-height: 28px;
    letter-spacing: 1px;
  }
  .title-main {
    display: block;
    font-size: 62px;
    line-height: 52px;
    text-transform: uppercase;
    letter-spacing: 0;
  }
  .title-main + .title-main { margin-top: -2px; }
  .cover-artwork {
    position: absolute;
    left: 44px;
    top: 176px;
    width: 310px;
    height: 270px;
    background: radial-gradient(ellipse 50% 50% at 50% 52%,
      var(--crimson-light) 0%,
      var(--crimson) 38%,
      rgba(154,12,18,0.85) 62%,
      rgba(216,18,28,0.35) 82%,
      rgba(236,204,166,0) 100%);
  }
  .ground-band {
    position: absolute;
    left: 0;
    top: 400px;
    width: 100%;
    height: 163px;
  }
  .subtitle {
    position: absolute;
    left: 0;
    top: 467px;
    width: 100%;
    text-align: center;
    font-family: "Cinzel", serif;
    font-size: 13.5px;
    line-height: 20px;
    color: var(--gold-text);
    text-transform: uppercase;
    letter-spacing: 0.1px;
  }
</style>
</head>
<body>
<main class="canvas">
  <article class="book-cover">
    <h1 class="title">
      <span class="title-lead">Copper</span>
      <span class="title-main">Lantern</span>
      <span class="title-main">Path</span>
    </h1>

    <div class="cover-artwork" role="img" aria-label="Illustration: red ink-splatter brain outline representing the mindset, with a black silhouette of a ninja performing a high kick on a hilltop"></div>

    <svg class="ground-band" viewBox="0 0 398 163" preserveAspectRatio="none" aria-hidden="true">
      <path d="M0 27 C 40 24, 90 20, 130 12 C 160 6, 190 4, 220 6 C 260 9, 300 18, 340 24 C 365 27, 385 27, 398 27 L 398 163 L 0 163 Z" fill="var(--ink)"/>
    </svg>

    <p class="subtitle">
      Empower your mind to live fearlessly,<br>
      creating a life full of wealth,<br>
      health and success
    </p>
  </article>
</main>
</body>
</html>
```